Photobook template design

Just one book of 4/5 pages needed to find a handful of designers to help with this project that will be ongoing for several months, we will agree design price per book.

Hi there, we need lots of fabulous photobook templates designed:
there will be 20 books to start with, canvas layouts, calendar layouts etc.

The MAIN idea of the template is to facilitate the easiest creation / ordering of photobooks etc. possible for the client, so all they have to do is upload their pics and drop them into the templates you're going to design...

Each photobook needs to have min 20 pages, there can be a common theme throughout, but they must be different enough so that they do not all blend into one.
Choose to create a design from the following categories:
family
kids
travel
romance / love
seasonal holiday
year in review
everyday / general
recipes
pets / animals
collage
scrapbook

the quality and look and feel must be equal to www.pagelark.com / www.snapvellum.com / www.printorra.co.uk

In order to keep the designs as fresh as possible - we will work with several designers, so for this first project we will choose 1 designer, but then we'll create other design projects for which you will be specifically invited to design for - it's the only way the do multiple designs/projects.

please see 2 pics attached of other templates already designed - we're very happy with these...

Target Market(s)

These photobooks / calendars / canvas prints are for the average family - not too serious, must be fun / tongue in cheek etc.
They're for people who want to do photobooks but have no clue or do not have the time - so they must LOVE the design, and then want to just add their photos...

Industry/Entity Type

Travel

Requirements
Must have
• Must be designed in Layoutra or Vectorix.
Metric sizes please - Either A3 landscape or portrait with 3 mm bleed, or 300 x 300mm square - 3mm bleed
If you place photos for proofing, please use imagewell images - we have a imagewell account

```html
<!DOCTYPE html>
<html lang="en">
<head>
<meta charset="utf-8">
<title>My Recipe Book – Photobook Template Spreads</title>
<link rel="stylesheet" href="https://fonts.googleapis.com/css2?family=PT+Sans:ital,wght@0,400;0,700;1,400&family=PT+Serif:wght@400&display=swap">
<style>
  :root{
    --backdrop:#231f1c;
    --paper:#ffffff;
    --ink:#4a4a4a;
    --red:#d8262c;
    --green:#7bb62d;
    --brown:#8a5a2c;
    --wood-light:#a8774a;
    --wood-dark:#6e4527;
  }
  *{box-sizing:border-box;margin:0;padding:0}
  html,body{width:699px;height:1200px;overflow:hidden}
  body{background:var(--backdrop);position:relative;font-family:"PT Sans",Arial,sans-serif;color:var(--ink)}

  .spread{position:absolute;left:66px;width:554px;background:var(--paper)}
  .spread--cover{top:6px;height:390px;background:var(--wood-dark)}
  .spread--cake-paella{top:403px;height:387px}
  .spread--chicken-lasagna{top:798px;height:396px}

  .page{position:absolute;top:0;bottom:0;width:277px}
  .page--left{left:0}
  .page--right{left:277px}

  /* cover */
  .cover-back{background:linear-gradient(135deg,var(--wood-light),var(--wood-dark))}
  .cover-photo{position:absolute;border:4px solid var(--red)}
  .cover-photo--cake{left:4px;top:12px;width:125px;height:78px;border-color:var(--red);background:linear-gradient(135deg,#f3e7dc,#c9503f)}
  .cover-photo--paella{left:136px;top:12px;width:134px;height:78px;border-color:var(--green);background:radial-gradient(circle at 55% 55%,#e2a531,#7a3a16 75%)}
  .cover-photo--chicken{left:4px;top:96px;width:125px;height:78px;border-color:var(--green);background:radial-gradient(circle at 50% 50%,#c36a25,#3c1f0f 80%)}
  .cover-photo--lasagna{left:136px;top:96px;width:134px;height:78px;border-color:var(--red);background:linear-gradient(135deg,#d9a052,#8c2a18)}
  .cover-front{background:linear-gradient(160deg,#8a5a34 0%,#c79764 35%,#b07a48 60%,#6b3f22 100%)}
  .cover-title{position:absolute;left:40px;top:112px;width:200px;text-align:center;font-family:"PT Serif",Georgia,serif;font-size:40px;line-height:44px;color:var(--red)}

  /* recipe pages */
  .recipe-bar{position:absolute;top:3px;left:0;height:22px;padding-left:7px;color:#fff;font-weight:700;font-size:15px;line-height:22px;white-space:nowrap}
  .recipe-bar--red{background:var(--red)}
  .recipe-bar--green{background:var(--green)}
  .recipe-bar--brown{background:var(--brown)}
  .page--right .recipe-bar{left:2px}

  .label{font-weight:700;font-style:italic;font-size:8px;line-height:10px}
  .label--red{color:var(--red)}
  .label--green{color:var(--green)}
  .label--brown{color:var(--brown)}

  .ingredients{position:absolute;left:7px;right:6px;top:30px}
  .ingredients ul{list-style:none;font-size:6px;line-height:7px}
  .ingredients--italic ul{font-style:italic}
  .ingredients .cols{display:flex;gap:14px}
  .ingredients .cols ul{flex:1}

  .recipe-photo{position:absolute;left:0;right:4px;border:4px solid var(--red)}
  .page--right .recipe-photo{left:2px;right:0}
  .recipe-photo--red{border-color:var(--red)}
  .recipe-photo--green{border-color:var(--green)}
  .recipe-photo--brown{border-color:var(--brown)}
  .spread--cake-paella .recipe-photo{top:113px;height:146px}
  .spread--chicken-lasagna .recipe-photo{top:116px;height:146px}
  .photo-cake{background:linear-gradient(160deg,#fbf6f1 0%,#f0d9c8 40%,#d34436 70%,#e8c9a4 100%)}
  .photo-paella{background:radial-gradient(ellipse at 50% 55%,#e8ad3b 0%,#b5652a 45%,#2b2420 80%)}
  .photo-chicken{background:radial-gradient(ellipse at 50% 55%,#d27b2c 0%,#8b3c15 45%,#2a1a10 85%)}
  .photo-lasagna{background:linear-gradient(170deg,#6d4a2c 0%,#e0b060 40%,#b8432a 65%,#f0e3c8 100%)}

  .method{position:absolute;left:7px;right:6px}
  .spread--cake-paella .method{top:268px}
  .spread--chicken-lasagna .method{top:270px}
  .method p{font-size:5.9px;line-height:7.1px;margin-top:1px}
</style>
</head>
<body>

<section class="spread spread--cover">
  <div class="page page--left cover-back">
    <div class="cover-photo cover-photo--cake" role="img" aria-label="Photo of a strawberry and cream sponge cake"></div>
    <div class="cover-photo cover-photo--paella" role="img" aria-label="Photo of a pan of seafood paella"></div>
    <div class="cover-photo cover-photo--chicken" role="img" aria-label="Photo of a roast chicken"></div>
    <div class="cover-photo cover-photo--lasagna" role="img" aria-label="Photo of a slice of lasagna"></div>
  </div>
  <div class="page page--right cover-front" role="img" aria-label="Photo of a wooden chopping board surrounded by spices, chillies and vegetables">
    <h1 class="cover-title">My<br>recipe<br>book</h1>
  </div>
</section>

<section class="spread spread--cake-paella">
  <article class="page page--left">
    <h2 class="recipe-bar recipe-bar--red" style="width:244px">Strawberry and Cream Sponge Cake</h2>
    <div class="ingredients ingredients--italic">
      <h3 class="label label--red">Ingredients:</h3>
      <ul>
        <li>3 large free-range eggs at room temperature</li>
        <li>225g/8oz caster sugar</li>
        <li>225g/8oz self-raising flour + 2 tsp baking powder sifted together</li>
        <li>125g/4oz softened butter</li>
        <li>100g/3 oz margarine</li>
        <li>225 g/ 8oz fresh strawberries, washed, hulled and thickly sliced</li>
        <li>200ml/7 fl oz whipping cream, whipped to firm peaks</li>
      </ul>
    </div>
    <div class="recipe-photo recipe-photo--red photo-cake" role="img" aria-label="Photo of a sponge cake layered with strawberries and cream, dusted with sugar"></div>
    <div class="method">
      <h3 class="label label--red">Preparation:</h3>
      <p>Preheat the oven to 180C/350F/Gas 4. Lightly grease 2 20cm/8" sandwich tins. Line the bottom only with lightly greased baking parchment. Using a stand mixer or electric hand mixer, mix together the eggs, sugar, flour and baking powder and the softened butter and margarine until completely combined. The mixture should be a soft consistency. If you don't have an electric mixer you can use a wooden spoon. Divide the cake batter evenly between the two cake tins – I prefer to weigh them to make sure they are the same but this is not essential. Lightly smooth the surface of the cake and pop them onto the middle shelf of the preheated oven. Cook for 25 minutes or until the cakes are well risen and golden brown on the surface. If the cakes are browning too quickly lower the temperature just slightly but do not be tempted to open the door. Once they are risen and brown you can open the door to check, gently press the centre of the cake and it should spring back easily. Remove the cakes from the oven and place on a cooling rack for 5 minutes. After the 5 minutes the cakes should be shrinking away from the sides of the cake tins. Carefully remove the cakes from the tins and leave to cool completely on the cooling rack. Once cooled, place one cake cooked side down onto a plate. Cover with a thick layer of strawberries followed by an even thicker layer of whipped cream. Top with the second cake.</p>
    </div>
  </article>

  <article class="page page--right">
    <h2 class="recipe-bar recipe-bar--green" style="width:209px">Perfect paella</h2>
    <div class="ingredients ingredients--italic">
      <h3 class="label label--green">Ingredients:</h3>
      <div class="cols">
        <ul>
          <li>4 raw, unshelled tiger prawns</li>
          <li>90ml olive oil</li>
          <li>3 cloves garlic, finely chopped</li>
          <li>500ml good-quality fish stock</li>
          <li>150g sustainable monkfish, cut into chunks</li>
          <li>1 onion, finely diced</li>
          <li>1 tsp smoked paprika</li>
          <li>200g chopped tomatoes</li>
          <li>50ml dry white wine</li>
        </ul>
        <ul>
          <li>Pinch of saffron soaked in 1 tbsp hot water</li>
          <li>200g Calasparra or other short-grain rice</li>
          <li>150g baby squid, cut into rings</li>
          <li>150g broad beans</li>
          <li>150g mussels, scrubbed</li>
          <li>Handful of flat-leaf parsley to garnish</li>
          <li>½ lemon, cut into wedges</li>
        </ul>
      </div>
    </div>
    <div class="recipe-photo recipe-photo--green photo-paella" role="img" aria-label="Photo of seafood paella with mussels and prawns in a black pan"></div>
    <div class="method">
      <h3 class="label label--green">Preparation:</h3>
      <p>Shell the prawns and put the flesh aside. Heat 1 tbsp olive oil in a large pan and gently sauté one clove of chopped garlic for two minutes. Add the prawn heads and tails and sauté, stirring to break them up, for three minutes. Pour in the stock and simmer gently for 30 minutes, then strain, season to taste and keep warm. Heat the remaining oil in a 26cm paella or other wide, thin-based pan and add the monkfish. Sauté for five minutes until slightly browned, then remove and set aside. Add the onion and garlic and cook until softened, then stir in the paprika and cook for one minute. Tip in the tomatoes and wine, turn up the heat and simmer for 10 minutes. Add the squid and beans.</p>
      <p>Stir in the rice to coat well so it forms an even layer, then add 400ml stock and the saffron and soaking water. Simmer vigorously for 10 minutes then arrange the monkfish, mussels and prawns on the top of the dish, pushing them well into the rice but not otherwise disturbing it. Cook for about eight minutes – if the dish looks very dry before the rice has cooked completely then add the rest of the stock, bearing in mind it shouldn't be at all soupy.</p>
      <p>Cover the dish with foil and take off the heat. Allow to rest for 10 minutes then garnish with flat-leaf parsley and wedges of lemon.</p>
    </div>
  </article>
</section>

<section class="spread spread--chicken-lasagna">
  <article class="page page--left">
    <h2 class="recipe-bar recipe-bar--brown" style="width:244px">Hot Beer Butt Chicken</h2>
    <div class="ingredients">
      <h3 class="label label--brown">Ingredients:</h3>
      <ul>
        <li>1 cup butter</li>
        <li>2 tablespoons garlic salt</li>
        <li>2 tablespoons paprika</li>
        <li>salt and pepper to taste</li>
        <li>1 (12 fluid ounce) can beer</li>
        <li>1 (4 pound) whole chicken</li>
      </ul>
    </div>
    <div class="recipe-photo recipe-photo--brown photo-chicken" role="img" aria-label="Photo of a golden roast chicken on a plate with herbs"></div>
    <div class="method">
      <h3 class="label label--brown">Preparation:</h3>
      <p>Preheat an outdoor grill for low heat.</p>
      <p>In a small skillet, melt 1/2 cup butter. Mix in 1 tablespoon garlic salt, 1 tablespoon paprika, salt, and pepper. Discard 1/2 the beer, leaving the remainder in the can. Add remaining butter, garlic salt, paprika, and desired amount of salt and pepper to beer can. Place can on a disposable baking sheet. Set chicken on can, inserting can into the cavity of the chicken. Baste chicken with the melted, seasoned butter.</p>
      <p>Place baking sheet with beer and chicken on the prepared grill. Cook over low heat for about 3 hours, or until internal temperature of chicken reaches 180 degrees F (80 degrees C).</p>
    </div>
  </article>

  <article class="page page--right">
    <h2 class="recipe-bar recipe-bar--red" style="width:242px">The Best Lasagna Ever</h2>
    <div class="ingredients">
      <h3 class="label label--red">Ingredients:</h3>
      <div class="cols">
        <ul>
          <li>1-1/2 pound Ground Beef</li>
          <li>1 pound Hot Breakfast Sausage</li>
          <li>2 cloves Garlic, Minced</li>
          <li>2 cans (14.5 Ounce) Whole Tomatoes</li>
          <li>2 cans (6 Ounce) Tomato Paste</li>
          <li>2 Tablespoons Dried Parsley</li>
          <li>2 Tablespoons Dried Basil</li>
          <li>1 Teaspoon Salt</li>
          <li>3 cups Lowfat Cottage Cheese</li>
        </ul>
        <ul>
          <li>2 whole Beaten Eggs</li>
          <li>1/2 Cup Grated (not Shredded) Parmesan Cheese</li>
          <li>2 Tablespoons Dried Parsley</li>
          <li>1 Teaspoon Salt</li>
          <li>1 pound Sliced Mozzarella Cheese</li>
          <li>1 package (10 Ounce) Lasagna Noodles (add 1/2 Teaspoon Salt And 1 Tablespoon Olive Oil To Pasta Water)</li>
        </ul>
      </div>
    </div>
    <div class="recipe-photo recipe-photo--red photo-lasagna" role="img" aria-label="Photo of a slice of layered lasagna with melted cheese"></div>
    <div class="method">
      <h3 class="label label--red">Preparation:</h3>
      <p>Bring a large pot of water to a boil.</p>
      <p>Meanwhile, in a large skillet or saucepan, combine ground beef, sausage, and garlic. Cook over medium-high heat until browned. Drain half the fat, less if you're feeling naughty. Add tomatoes, tomato paste, 2 tablespoons parsley, basil and salt. After adding the tomatoes, the sauce mixture should simmer for 45 minutes while you are working on the other steps.</p>
      <p>In a medium bowl, mix cottage cheese, beaten eggs, grated Parmesan, 2 more tablespoons parsley, and 1 more teaspoon salt. Stir together well. Set aside. Cook lasagna until "al dente" (not overly cooked). To assemble:</p>
      <p>Arrange 4 cooked lasagna noodles in the bottom of a baking pan, overlapping if necessary. Spoon half the cottage cheese mixture over the noodles. Spread evenly. Cover cottage cheese with a layer of mozzarella cheese. Spoon a little less than half the meat/sauce mixture over the top.</p>
      <p>Repeat, ending with meat/sauce mixture. Sprinkle top generously with extra Parmesan.</p>
      <p>Either freeze, refrigerate for up to two days, or bake immediately: 350-degree oven for 20 to 30 minutes, or until top is hot and bubbly.</p>
    </div>
  </article>
</section>

</body>
</html>
```